Business card for my company-RMK Design Studio

I do not have a logo-I like red and keeping it clean. Information that should be on the card:
Tom Brakefield AIA
Architecture Planning Interiors
Cell Phone-614.492.5068
email-rmkarchitect1@lunvale.com
www.rmkdesignstudio.net

```html
<!DOCTYPE html>
<html lang="en">
<head>
<meta charset="utf-8">
<title>RMK Design Studio – Business Card</title>
<link rel="stylesheet" href="https://fonts.googleapis.com/css2?family=Jost:wght@400;500;700;800&display=swap">
<style>
  :root {
    --brand-red: #e2001f;
    --paper: #ffffff;
    --ink: #2a2a2a;
    --backdrop: #e0e0e0;
    --shadow: rgba(0, 0, 0, 0.14);
  }
  * { box-sizing: border-box; margin: 0; padding: 0; }
  html, body {
    width: 1134px; height: 1200px; overflow: hidden;
    background: var(--backdrop);
    font-family: "Jost", "Futura", sans-serif;
  }
  .canvas { position: relative; width: 1134px; height: 1200px; }

  .card {
    position: absolute; left: 187px; width: 760px; height: 434px;
    box-shadow: 0 6px 18px var(--shadow);
    overflow: hidden;
  }
  .card--front { top: 56px; background: var(--brand-red); }
  .card--back { top: 530px; background: var(--paper); }

  /* wordmark */
  .wordmark {
    display: flex; align-items: center; gap: 14px;
    font-weight: 500; letter-spacing: 0.12em; text-transform: uppercase;
    white-space: nowrap;
  }
  .wordmark__square { width: 22px; height: 22px; flex: none; }

  .card--front .wordmark {
    position: absolute; left: 50%; top: 50%; transform: translate(-50%, -50%);
    color: var(--paper); font-size: 34px;
  }
  .card--front .wordmark__square { background: var(--paper); }

  .card__panel { position: absolute; inset: 0; }

  .identity { position: absolute; left: 48px; top: 92px; width: 380px; }
  .identity .wordmark { color: var(--brand-red); font-size: 27px; }
  .identity .wordmark__square { background: var(--brand-red); }
  .identity__rule {
    width: 80px; height: 3px; background: var(--brand-red);
    margin: 34px 0 30px 36px;
  }
  .identity__name { color: var(--ink); font-size: 36px; line-height: 1; }
  .identity__name strong { font-weight: 800; }
  .identity__name span { font-weight: 400; }
  .identity__role { color: var(--ink); font-size: 20px; margin-top: 6px; }

  .contact {
    position: absolute; left: 495px; top: 62px; width: 250px;
    color: var(--paper); list-style: none;
  }
  .contact__item {
    display: flex; align-items: flex-start; gap: 12px;
    font-size: 15.5px; line-height: 1.25; margin-bottom: 14px;
  }
  .contact__icon {
    flex: none; width: 26px; height: 26px; border-radius: 50%;
    background: var(--paper); display: flex; align-items: center; justify-content: center;
  }
  .contact__icon svg { width: 14px; height: 14px; fill: var(--brand-red); }
  .contact__text strong { font-weight: 500; display: block; }

  .lockup {
    position: absolute; left: 0; right: 0; top: 1040px;
    display: flex; justify-content: center;
  }
  .lockup .wordmark { color: var(--brand-red); font-size: 44px; }
  .lockup .wordmark__square { width: 30px; height: 30px; background: var(--brand-red); }
</style>
</head>
<body>
<main class="canvas">

  <section class="card card--front" aria-label="Card front">
    <div class="wordmark"><span class="wordmark__square"></span>RMK Design Studio</div>
  </section>

  <section class="card card--back" aria-label="Card back">
    <svg class="card__panel" viewBox="0 0 760 434" aria-hidden="true">
      <path d="M470 0 H760 V434 H0 V398 H410 A60 60 0 0 0 470 338 Z" fill="var(--brand-red)"/>
    </svg>

    <div class="identity">
      <div class="wordmark"><span class="wordmark__square"></span>RMK Design Studio</div>
      <div class="identity__rule"></div>
      <p class="identity__name"><strong>Daniel</strong> <span>Reyes</span></p>
      <p class="identity__role">Project Manager</p>
    </div>

    <ul class="contact">
      <li class="contact__item">
        <span class="contact__icon"><svg viewBox="0 0 24 24"><path d="M12 2a7 7 0 0 0-7 7c0 5 7 13 7 13s7-8 7-13a7 7 0 0 0-7-7zm0 9.5A2.5 2.5 0 1 1 12 6.5a2.5 2.5 0 0 1 0 5z"/></svg></span>
        <span class="contact__text"><strong>Tom Brakefield AIA</strong>Architecture Planning Interiors</span>
      </li>
      <li class="contact__item">
        <span class="contact__icon"><svg viewBox="0 0 24 24"><path d="M6.6 10.8a15 15 0 0 0 6.6 6.6l2.2-2.2a1 1 0 0 1 1-.25 11.4 11.4 0 0 0 3.6.57 1 1 0 0 1 1 1V20a1 1 0 0 1-1 1A17 17 0 0 1 3 4a1 1 0 0 1 1-1h3.5a1 1 0 0 1 1 1c0 1.25.2 2.45.57 3.6a1 1 0 0 1-.25 1z"/></svg></span>
        <span class="contact__text">614.492.5068</span>
      </li>
      <li class="contact__item">
        <span class="contact__icon"><svg viewBox="0 0 24 24"><path d="M3 5h18v14H3zm2 2v.5l7 5 7-5V7l-7 5z"/></svg></span>
        <span class="contact__text">rmkarchitect1@lunvale.com</span>
      </li>
      <li class="contact__item">
        <span class="contact__icon"><svg viewBox="0 0 24 24"><path d="M12 3l7 18-7-4-7 4z"/></svg></span>
        <span class="contact__text">www.rmkdesignstudio.net</span>
      </li>
    </ul>
  </section>

  <div class="lockup">
    <div class="wordmark"><span class="wordmark__square"></span>RMK Design Studio</div>
  </div>

</main>
</body>
</html>
```